Web Design Project

site will be : www.chatbridgenow.example
We are a new business specialising in providing online customer support and sales services for a wide range of business types.

Will have to source suitable stock shots for images.
will also souce sample graphics of service, to follow.
Updates

Project Deadline Extended
Reason: This should allow enough time for any outstanding designs to be submitted. We are keen to press on so Further extension will only be considered if the designer contacts me with a very good reason.

Target Market(s)

Online Businesses

Industry/Entity Type

Business

Requirements
Must have
• Quick Assist Button....see briefing document for further details

```html
<!DOCTYPE html>
<html lang="en">
<head>
<meta charset="utf-8">
<title>Quick Assist Express</title>
<link rel="stylesheet" href="https://fonts.googleapis.com/css2?family=Noto+Sans:wght@400;700&display=swap">
<style>
  :root {
    --page-dark: #7d7d7d;
    --page-light: #dcdcdc;
    --ink: #2a2a2a;
    --body-text: #555555;
    --accent: #2f7fb8;
    --nav-top: #4a4a4a;
    --nav-bottom: #262626;
    --nav-text: #e8e8e8;
    --button-top: #3c6a93;
    --button-bottom: #1f4567;
    --footer-band: #3a3a3a;
    --footer-panel: #264a72;
    --footer-text: #e6edf5;
    --footer-muted: #aac4e0;
    --footer-rule: #5476a0;
    --tick: #2b8fc8;
    --status-green: #3fbf3a;
    --status-bubble: #2d8fc4;
    --hero-light: #e6f4fb;
    --hero-mid: #8fcbe6;
    --hero-deep: #3d9ac4;
  }
  * { box-sizing: border-box; margin: 0; padding: 0; }
  html, body { width: 1200px; height: 1064px; overflow: hidden; }
  body {
    position: relative;
    font-family: "Noto Sans", Verdana, sans-serif;
    background:
      radial-gradient(ellipse 700px 600px at 600px 560px, var(--page-light) 0%, #c4c4c4 55%, var(--page-dark) 100%);
  }
  .abs { position: absolute; }

  /* Header */
  .brand {
    left: 244px; top: 22px; width: 200px; height: 44px;
    display: flex; align-items: center; gap: 8px;
    font-size: 20px; font-weight: 700; color: #1e1e1e; line-height: 1.05;
  }
  .brand-mark { width: 14px; height: 14px; background: #1e1e1e; flex: none; }
  .status-button {
    left: 753px; top: 16px; width: 204px; height: 60px;
    display: flex; align-items: center;
  }
  .status-dot {
    width: 44px; height: 44px; border-radius: 50%;
    background: var(--status-green); flex: none; margin-right: -10px; z-index: 1;
    border: 3px solid #1e6e1a;
  }
  .status-bubble {
    flex: 1; height: 44px; background: var(--status-bubble); border-radius: 4px;
    padding: 5px 6px 0 18px; color: #fff;
  }
  .status-title { font-size: 14px; font-weight: 700; line-height: 1.1; }
  .status-title span { color: #8ef07a; }
  .status-sub { font-size: 8px; line-height: 1.3; }

  /* Navigation */
  .main-nav {
    left: 244px; top: 84px; width: 713px; height: 44px;
    background: linear-gradient(var(--nav-top), var(--nav-bottom));
    display: flex; align-items: center; padding-left: 25px;
  }
  .main-nav a {
    color: var(--nav-text); text-decoration: none; font-size: 12px;
    padding-right: 20px; margin-right: 22px; border-right: 1px solid #5c5c5c; line-height: 10px;
  }
  .main-nav a:last-child { border-right: none; }

  /* Hero */
  .hero {
    left: 244px; top: 128px; width: 713px; height: 183px;
    background: linear-gradient(100deg, var(--hero-deep) 0%, var(--hero-mid) 35%, var(--hero-light) 62%, #f4f4f4 100%);
  }
  .hero-headline {
    left: 279px; top: 205px; font-size: 23px; color: #fff;
  }
  .hero-arrow {
    top: 196px; width: 24px; height: 47px; background: #f2f2f2;
    border: 1px solid #c8c8c8;
  }

  /* Services */
  .services {
    left: 244px; top: 311px; width: 713px; height: 162px;
    display: flex; background: #f7f7f7;
  }
  .service {
    flex: 1; padding: 24px 0 0 27px;
    background: linear-gradient(#ffffff, #ededed);
    border-right: 1px solid #d6d6d6;
  }
  .service:last-child { border-right: none; }
  .service-title { display: flex; align-items: center; gap: 8px; font-size: 16px; color: var(--ink); height: 30px; }
  .service p {
    margin-top: 4px; width: 186px; font-size: 9.5px; line-height: 16.5px; color: var(--body-text);
  }
  .read-more {
    display: inline-block; margin-top: 8px; width: 90px; height: 20px;
    background: linear-gradient(var(--button-top), var(--button-bottom));
    color: #fff; font-size: 8px; text-align: center; line-height: 20px; text-decoration: none;
  }

  /* Content */
  .content {
    left: 244px; top: 473px; width: 713px; height: 398px;
    background: linear-gradient(#f4f4f4, #e2e2e2);
  }
  .section-title { font-size: 19px; color: var(--ink); font-weight: 400; }
  .section-title span { color: var(--accent); }
  .welcome { left: 272px; top: 497px; width: 432px; }
  .welcome .lead { margin-top: 8px; font-size: 9.5px; color: var(--body-text); }
  .welcome .body {
    margin-top: 16px; font-size: 9.5px; line-height: 17px; color: var(--body-text);
  }
  .welcome ul { list-style: none; margin-top: 15px; }
  .welcome li {
    height: 33px; line-height: 33px; border-bottom: 1px solid #cfcfcf;
    font-size: 10px; font-weight: 700; color: var(--accent); padding-left: 16px; position: relative;
  }
  .welcome li::before {
    content: ""; position: absolute; left: 2px; top: 14px; width: 5px; height: 5px;
    border-radius: 50%; background: #8fb4d0;
  }

  .why { left: 727px; top: 497px; width: 197px; }
  .why ul { list-style: none; margin-top: 22px; }
  .why li {
    position: relative; padding: 0 0 10px 20px; margin-bottom: 9px;
    border-bottom: 1px solid #d2d2d2; font-size: 9.5px; line-height: 17px; color: var(--body-text);
  }
  .why li:last-child { border-bottom: none; }
  .why li svg { position: absolute; left: 2px; top: 4px; }

  /* Footer */
  .footer-band { left: 0; top: 871px; width: 1200px; height: 193px; background: var(--footer-band); }
  .footer-panel { left: 244px; top: 871px; width: 713px; height: 193px; background: var(--footer-panel); }
  .footer-heading { font-size: 16px; color: var(--footer-text); font-weight: 400; }
  .footer-links { left: 277px; top: 889px; width: 208px; }
  .footer-links ul { list-style: none; margin-top: 12px; }
  .footer-links li {
    height: 22px; line-height: 22px; font-size: 9.5px; color: var(--footer-muted);
    border-bottom: 1px solid var(--footer-rule); padding-left: 12px; position: relative;
  }
  .footer-links li:last-child { border-bottom: none; }
  .footer-links li::before {
    content: "›"; position: absolute; left: 0; top: -1px; color: #fff; font-size: 14px; font-weight: 700;
  }
  .follow { left: 523px; top: 889px; }
  .social { display: flex; gap: 19px; margin-top: 22px; margin-left: 0; }
  .social span {
    width: 36px; height: 36px; border-radius: 50%;
    background: radial-gradient(circle at 40% 35%, #6fb5e6, #2a74b4);
    border: 3px solid #dfe9f3;
  }
  .contact { left: 795px; top: 889px; width: 150px; }
  .contact p { font-size: 9.5px; color: var(--footer-text); line-height: 16.7px; }
  .contact p:first-of-type { margin-top: 12px; }
  .contact .value { color: var(--footer-muted); }
  .contact .mail { color: #e8c640; }
  .copyright { left: 275px; top: 1025px; font-size: 9.5px; color: var(--footer-text); }
</style>
</head>
<body>

  <header>
    <div class="abs brand"><span class="brand-mark"></span>Quick Assist<br>Express</div>
    <div class="abs status-button">
      <span class="status-dot"></span>
      <div class="status-bubble">
        <div class="status-title">Quick Assist Is <span>Open</span></div>
        <div class="status-sub">Speak with a support representative</div>
      </div>
    </div>
    <nav class="abs main-nav">
      <a href="#">Home</a><a href="#">Services</a><a href="#">About Us</a><a href="#">FAQ</a><a href="#">Pricing</a><a href="#">Contact Us</a>
    </nav>
  </header>

  <div class="abs hero" role="img" aria-label="Photo of two smiling support agents wearing headsets"></div>
  <div class="abs hero-headline">Want to close more online sales?</div>
  <div class="abs hero-arrow" style="left:239px">
    <svg width="22" height="45" viewBox="0 0 22 45"><path d="M13 16 L8 22.5 L13 29" fill="none" stroke="#999" stroke-width="1.5"/></svg>
  </div>
  <div class="abs hero-arrow" style="left:939px">
    <svg width="22" height="45" viewBox="0 0 22 45"><path d="M9 16 L14 22.5 L9 29" fill="none" stroke="#999" stroke-width="1.5"/></svg>
  </div>

  <section class="abs services">
    <div class="service">
      <div class="service-title">
        <svg width="34" height="28" viewBox="0 0 34 28"><ellipse cx="17" cy="12" rx="15" ry="10" fill="#5aa5d8" stroke="#2f6f9e" stroke-width="1.5"/><path d="M10 20 L7 27 L16 21" fill="#5aa5d8" stroke="#2f6f9e" stroke-width="1.5"/></svg>
        Live Chat.
      </div>
      <p>Our professional team will instantly deal with any queries your visitors have, ensuring no potential sales are unnecessarily lost.</p>
      <a class="read-more" href="#">READ MORE</a>
    </div>
    <div class="service">
      <div class="service-title">
        <svg width="28" height="30" viewBox="0 0 28 30"><rect x="6" y="2" width="18" height="26" fill="#f4f4f4" stroke="#8a8a8a"/><path d="M10 9h10M10 13h10M10 17h10M10 21h7" stroke="#aaa"/><rect x="2" y="6" width="5" height="22" fill="#777"/></svg>
        Email Tickets.
      </div>
      <p>We can handle all your email communications ensuring all queries are dealt with in a prompt and professional manner.</p>
      <a class="read-more" href="#">READ MORE</a>
    </div>
    <div class="service">
      <div class="service-title">
        <svg width="34" height="28" viewBox="0 0 34 28"><rect x="2" y="6" width="30" height="20" fill="#f2f2f2" stroke="#8a8a8a"/><path d="M2 6 L17 17 L32 6" fill="none" stroke="#8a8a8a"/></svg>
        Newsletters.
      </div>
      <p>We can help you maintain relationships with your existing customers by managing your email marketing campaign.</p>
      <a class="read-more" href="#">READ MORE</a>
    </div>
  </section>

  <main>
    <div class="abs content"></div>

    <section class="abs welcome">
      <h1 class="section-title">Welcome to <span>Quick Assist Express</span>!</h1>
      <p class="lead">Based in Ireland with European agents to cater for a European market.</p>
      <p class="body">Vivamus eget erat turpis, in viverra neque. Sed congue mattis nunc, eget dictum lorem hendrerit eu. Integer tempor pretium ligula, a sagittis eros mollis vitae. Phasellus fringilla tincidunt nisi, id mollis augue fringilla ut. Proin porttitor dictum magna, vel pretium tortor pulvinar eget. Vestibulum porta tortor vitae magna fringilla non ullamcorper justo imperdiet. Integer porta venenatis neque, eu placerat enim scelerisque vel. Aliquam erat volutpat. In hendrerit, neque nec rutrum hendrerit, eros purus congue nibh, ut luctus diam magna quis libero. Aenean et augue non libero dapibus iaculis. Praesent rutrum sapien eget nunc fermentum feugiat. In hac habitasse platea dictumst. Duis sodales imperdiet nisi in tincidunt. Maecenas rhoncus imperdiet arcu, in bibendum est pulvinar ac. Maecenas non nisi mauris.</p>
      <ul>
        <li>Aliquam erat volutpat.</li>
        <li>Duis sodales imperdiet nisi in tincidunt.</li>
        <li>Nam et egestas lorem.</li>
      </ul>
    </section>

    <section class="abs why">
      <h2 class="section-title">Why <span>Quick Assist</span>?</h2>
      <ul>
        <li><svg width="11" height="9" viewBox="0 0 11 9"><path d="M1 4.5 L4 7.5 L10 1" fill="none" stroke="#2b8fc8" stroke-width="2"/></svg>Convert visitors to your website into customers</li>
        <li><svg width="11" height="9" viewBox="0 0 11 9"><path d="M1 4.5 L4 7.5 L10 1" fill="none" stroke="#2b8fc8" stroke-width="2"/></svg>Improve Customer Communication</li>
        <li><svg width="11" height="9" viewBox="0 0 11 9"><path d="M1 4.5 L4 7.5 L10 1" fill="none" stroke="#2b8fc8" stroke-width="2"/></svg>Monitor visitors to your website in real time</li>
        <li><svg width="11" height="9" viewBox="0 0 11 9"><path d="M1 4.5 L4 7.5 L10 1" fill="none" stroke="#2b8fc8" stroke-width="2"/></svg>Work closely with you to identify your support requirements</li>
        <li><svg width="11" height="9" viewBox="0 0 11 9"><path d="M1 4.5 L4 7.5 L10 1" fill="none" stroke="#2b8fc8" stroke-width="2"/></svg>Provide professional agents to implement those requirements</li>
        <li><svg width="11" height="9" viewBox="0 0 11 9"><path d="M1 4.5 L4 7.5 L10 1" fill="none" stroke="#2b8fc8" stroke-width="2"/></svg>Reduce your operational costs</li>
        <li><svg width="11" height="9" viewBox="0 0 11 9"><path d="M1 4.5 L4 7.5 L10 1" fill="none" stroke="#2b8fc8" stroke-width="2"/></svg>Provide detailed website traffic reports</li>
      </ul>
    </section>
  </main>

  <footer>
    <div class="abs footer-band"></div>
    <div class="abs footer-panel"></div>
    <div class="abs footer-links">
      <h3 class="footer-heading">A List Of Links</h3>
      <ul>
        <li>Sed non orci et justo.</li>
        <li>Quis fringilla elit.</li>
        <li>Lorem ipsum dolor sit amet.</li>
        <li>Nunc fringilla.</li>
      </ul>
    </div>
    <div class="abs follow">
      <h3 class="footer-heading">Follow Us On:</h3>
      <div class="social"><span></span><span></span><span></span></div>
    </div>
    <div class="abs contact">
      <h3 class="footer-heading">Contact us</h3>
      <p>34000 Your City, Your adress</p>
      <p>Phone: <span class="value">800.00.000</span></p>
      <p>Fax: <span class="value">800.00.000</span></p>
      <p>E-mail: <span class="mail">mail@mail.mail</span></p>
    </div>
    <p class="abs copyright">Copyright © 2011-2012 Quick Assist Express. All rights reserved.</p>
  </footer>

</body>
</html>
```